Flashy and colorful banner for an orange grower

Hi, I need a graphic for an advertising banner (80x200cm) to be placed next to the sales van. So far we have tried to highlight the naturalness of our products. With this banner we would like to highlight the ancient Sicilian tradition, with the typical decorations, I attach some photos as an example. We will sell our products far from Sicily, so I would like to exalt our origin.
We would like to dare with a colorful and amazing design, to capture the attention of passers-by.
It might be nice to insert or rework the decoration within our logo.
I would like to insert 4 of our offers inside the banner, only in the upper part, from the middle up.
The text is:
DAL CUORE DELLA SICILIA
ARANCIA TAROCCO
ALLA RINFUSA
5€ BORSA
DA SPREMERE
10€ CASSETTA
DA TAVOLA
15€ CASSETTA
SELEZIONE PREMIUM
20€ CASSETTA
Thanks for your time

```html
<!DOCTYPE html>
<html lang="it">
<head>
<meta charset="utf-8">
<title>Banner arance</title>
<link rel="stylesheet" href="https://fonts.googleapis.com/css2?family=Anton&family=Roboto:wght@400;500;900&display=swap">
<style>
  :root{
    --stage:#5c5c5c;
    --white:#ffffff;
    --green:#1f7a3c;
    --green-dark:#146c3a;
    --green-light:#5dbb46;
    --orange:#f4831f;
    --orange-deep:#e8562a;
    --yellow:#e2e04e;
  }
  *{margin:0;padding:0;box-sizing:border-box}
  html,body{width:1200px;height:2609px;overflow:hidden;background:var(--stage)}
  .banner{position:absolute;left:163px;top:170px;width:882px;height:2200px;overflow:hidden;background:var(--white);font-family:'Roboto',sans-serif}
  .bands{position:absolute;inset:0}
  .brand{position:absolute;left:0;width:882px;top:0;height:380px}
  .brand-mark{position:absolute;left:354px;top:80px;width:132px;height:132px;border-radius:50%;background:var(--orange)}
  .brand-name{position:absolute;left:0;width:882px;top:228px;text-align:center;font-weight:500;font-size:42px;letter-spacing:1px;color:var(--green-dark);line-height:1.2}

  /* Decorative areas: soft tonal fields, kept light so the offers and fruit stay on top */
  .ornament-top{position:absolute;top:42px;width:106px;height:375px;border-radius:90px 18px 90px 18px;opacity:.9}
  .ornament-top.left{left:20px;background:linear-gradient(160deg,#4aa648 0%,var(--green) 42%,#f06a2c 58%,var(--orange-deep) 100%)}
  .ornament-top.right{left:738px;background:linear-gradient(200deg,#4aa648 0%,var(--green) 42%,#f06a2c 58%,var(--orange-deep) 100%)}
  .ornament-column{position:absolute;top:470px;width:84px;height:1560px;border-radius:42px;
    background:linear-gradient(90deg,rgba(255,255,255,0) 0%,rgba(255,255,255,.22) 50%,rgba(255,255,255,0) 100%)}
  .ornament-column.left{left:24px}
  .ornament-column.right{left:750px}
  .ornament-bottom{position:absolute;left:80px;top:2075px;width:560px;height:70px;border-radius:35px;
    background:linear-gradient(90deg,rgba(255,255,255,0) 0%,rgba(255,255,255,.3) 50%,rgba(255,255,255,0) 100%)}

  .headline{position:absolute;left:0;width:882px;top:408px;text-align:center;font-family:'Anton',sans-serif;color:var(--white);font-size:86px;line-height:94px;letter-spacing:1px;text-transform:uppercase}
  .slice{position:absolute;border-radius:50%;background:radial-gradient(circle,#fbb94a 0%,var(--orange) 75%,#f7c27a 100%);box-shadow:4px 6px 10px rgba(0,0,0,.35)}
  .offer{position:absolute;left:0;width:882px;text-align:center;color:var(--white)}
  .offer-label{font-weight:400;font-size:40px;line-height:48px;height:48px}
  .offer-price{margin:14px auto 0;width:226px;height:150px;border-radius:50%;display:flex;align-items:center;justify-content:center;font-weight:900;font-size:96px;letter-spacing:-4px;color:var(--green-dark)}
  .offer-price.yellow{background:var(--yellow)}
  .offer-price.white{background:var(--white)}
  .offer-unit{margin-top:12px;font-weight:900;font-size:48px;line-height:56px}
</style>
</head>
<body>
<div class="banner">
  <svg class="bands" width="882" height="2200" viewBox="0 0 882 2200">
    <defs>
      <linearGradient id="green-top" x1="0" y1="0" x2="0" y2="1">
        <stop offset="0" stop-color="#1d7a3b"/><stop offset="1" stop-color="#2a8a3f"/>
      </linearGradient>
      <linearGradient id="orange-band" x1="0" y1="0" x2="0" y2="1">
        <stop offset="0" stop-color="#f4861f"/><stop offset="1" stop-color="#ef7722"/>
      </linearGradient>
      <linearGradient id="green-bottom" x1="0" y1="0" x2="0" y2="1">
        <stop offset="0" stop-color="#146c3a"/><stop offset=".45" stop-color="#2a8a3f"/><stop offset="1" stop-color="#5dbb46"/>
      </linearGradient>
    </defs>
    <path d="M0,450 Q441,322 882,450 L882,2200 L0,2200Z" fill="url(#green-top)"/>
    <path d="M0,765 Q441,675 882,765 L882,2200 L0,2200Z" fill="url(#orange-band)"/>
    <path d="M0,1095 Q441,1005 882,1095 L882,2200 L0,2200Z" fill="var(--green-dark)"/>
    <path d="M0,1420 Q441,1330 882,1420 L882,2200 L0,2200Z" fill="url(#orange-band)"/>
    <path d="M0,1745 Q441,1665 882,1745 L882,2200 L0,2200Z" fill="url(#green-bottom)"/>
  </svg>

  <div class="brand">
    <div class="brand-mark"></div>
    <div class="brand-name">SOLEVERDE SICILIA</div>
  </div>
  <div class="ornament-top left" role="img" aria-label="Traditional Sicilian scroll ornament in green and orange"></div>
  <div class="ornament-top right" role="img" aria-label="Traditional Sicilian scroll ornament in green and orange"></div>

  <div class="ornament-column left" role="img" aria-label="White traditional Sicilian scroll border"></div>
  <div class="ornament-column right" role="img" aria-label="White traditional Sicilian scroll border"></div>
  <div class="ornament-bottom" role="img" aria-label="White traditional Sicilian scroll flourish"></div>

  <h1 class="headline">Dal cuore della<br>Sicilia<br>Arancia Tarocco</h1>

  <div class="slice" style="left:680px;top:880px;width:200px;height:250px" role="img" aria-label="Orange slice photo"></div>
  <div class="slice" style="left:637px;top:1100px;width:240px;height:240px" role="img" aria-label="Orange wedges photo"></div>
  <div class="slice" style="left:-40px;top:1115px;width:248px;height:250px" role="img" aria-label="Orange slice photo"></div>
  <div class="slice" style="left:-90px;top:1660px;width:260px;height:260px" role="img" aria-label="Orange wedge photo"></div>
  <div class="slice" style="left:-40px;top:1915px;width:257px;height:255px" role="img" aria-label="Orange slice photo"></div>
  <div class="slice" style="left:710px;top:1600px;width:220px;height:320px" role="img" aria-label="Orange slice photo"></div>
  <div class="slice" style="left:607px;top:1880px;width:260px;height:290px" role="img" aria-label="Orange wedges photo"></div>

  <div class="offer" style="top:744px">
    <div class="offer-label">ALLA RINFUSA</div>
    <div class="offer-price yellow">5€</div>
    <div class="offer-unit">BORSA</div>
  </div>
  <div class="offer" style="top:1066px">
    <div class="offer-label">DA SPREMERE</div>
    <div class="offer-price white">10€</div>
    <div class="offer-unit">CASSETTA</div>
  </div>
  <div class="offer" style="top:1396px">
    <div class="offer-label">DA TAVOLA</div>
    <div class="offer-price yellow">15€</div>
    <div class="offer-unit">CASSETTA</div>
  </div>
  <div class="offer" style="top:1746px">
    <div class="offer-label">SELEZIONE PREMIUM</div>
    <div class="offer-price white">20€</div>
    <div class="offer-unit">CASSETTA</div>
  </div>
</div>
</body>
</html>
```